2 x Digitize Logo | 2 x Business Cards | 2 x Fridge Magnets

We require 6 deliverables:
1. Residential logo redrawn (same just high quality for large print format).
2. Corporate logo redrawn (minor changes to wording and high quality for large print format).
3. New business card design for Furniture Removals (residential)
4. New business card design for Corporate Relocations (business)
5. New Fridge magnet for Furniture removals (residential)
6. New fridge magnet for Corporate Relocations (business)
1. Residential Logo
a. We require the logo to be translated into a high quality digital image with no modifications.
2. Residential Logo
a. We require the logo to be edited (add the word corporate relocations) be translated into a high quality digital image.
3. Using the resilogo please make a new business card for our business.
a. Please see the web site https://www.brightlanehaulage.com.au for colours and inspiration.
b. The residential business card needs the following information:
i. Business Name (using the residential logo).
ii. Free Call: 1800 BL Haul (the Q, P and Move much be the same colour as the logo).
iii. Website: www.BrightLaneHaulage.com.au
iv. Address: 4/7 Ashgrove Court, VIC 3521
v. Email: move@BrightLaneHaulage.com.au
vi. backof Card:
Review our service
www.RateYourStay.com.au
Services: Local, Country, Interstate | Furniture Removals | Piano, Billiard Tables & Antiques
4. Using the corplogo please make a new business card for our business.
b. The corporate business card needs the following information:
i. Business Name (using the corporate logo).
v. Email: corporate@BrightLaneHaulage.com.au
vi. Back of Card:
Review our service
www.RateYourStay.com.au
Services: Corporate relocations | Office equipment moves | Packing Service | Packing Materials
5. Using the resilogo please make a new fridge magent for our business.
b. The residential fidge magnet needs the following information:
iv. Services: Local, Country, Interstate | Furniture Removals | Piano, Billiard Tables & Antiques
6. Using the corplogo please make a new fridge magent for our business.
b. The corporate fidge magnet needs the following information:
iv. Services: Local, Country, Interstate | Corporate relocations
Target Market(s)
Residential Furniture Removals and Corporate Office relocations
Industry/Entity Type
Business
Contact Information for Business Card
Please see full brief for six items required
Requirements
Must have
- Clean simple, easy to read
Nice to have
- fresh, stand out, eye catching
Should not have
- plain, standard, boring, general

```html
<!DOCTYPE html>
<html lang="en">
<head>
<meta charset="utf-8">
<title>Bright Lane Haulage – Business Card</title>
<link rel="stylesheet" href="https://fonts.googleapis.com/css2?family=Open+Sans:wght@400;600;700&display=swap">
<style>
  :root {
    --bg: #e9e9e9;
    --green: #55bd72;
    --yellow: #f6bd16;
    --red: #e2262b;
    --ink: #555555;
    --white: #ffffff;
  }
  * { box-sizing: border-box; margin: 0; padding: 0; }
  html, body {
    width: 1200px;
    height: 964px;
    overflow: hidden;
    background: var(--bg);
    font-family: "Open Sans", Arial, sans-serif;
  }
  .canvas {
    width: 1200px;
    height: 964px;
    display: flex;
    flex-direction: column;
    align-items: center;
    justify-content: center;
    gap: 40px;
  }
  .card {
    position: relative;
    width: 700px;
    height: 400px;
    overflow: hidden;
    box-shadow: 0 6px 18px rgba(0,0,0,0.18);
  }
  /* Back of card */
  .card--back {
    background: var(--green);
    display: flex;
    flex-direction: column;
    align-items: center;
    justify-content: center;
    text-align: center;
    color: var(--white);
  }
  .services-title {
    color: var(--yellow);
    font-size: 30px;
    font-weight: 400;
    margin-bottom: 14px;
  }
  .services-list {
    font-size: 19px;
    line-height: 1.35;
  }
  /* Front of card */
  .card--front { background: var(--white); }
  .swoosh {
    position: absolute;
    inset: 0;
    width: 100%;
    height: 100%;
  }
  .brand {
    position: absolute;
    left: 36px;
    top: 152px;
    display: flex;
    align-items: center;
    gap: 10px;
    color: var(--green);
    font-size: 26px;
    font-weight: 700;
    line-height: 1.2;
    letter-spacing: 0.3px;
    text-transform: uppercase;
    white-space: nowrap;
  }
  .brand-dot {
    width: 14px;
    height: 14px;
    border-radius: 50%;
    background: var(--yellow);
    flex: none;
  }
  .contact {
    position: absolute;
    right: 40px;
    top: 60px;
    text-align: right;
    color: var(--ink);
    font-size: 17px;
    font-style: normal;
    line-height: 1.55;
    white-space: nowrap;
  }
  .contact-phone {
    color: var(--green);
    font-size: 20px;
  }
</style>
</head>
<body>
<main class="canvas">
  <section class="card card--back">
    <h2 class="services-title">Services:</h2>
    <p class="services-list">Local, Country, Interstate &nbsp;|&nbsp; Furniture Removals<br>Piano, Billiard Tables &amp; Antiques</p>
  </section>

  <section class="card card--front">
    <svg class="swoosh" viewBox="0 0 700 400" preserveAspectRatio="none" aria-hidden="true">
      <path fill="var(--green)" d="M0,345 C180,290 420,245 700,225 V400 H0 Z"/>
      <path fill="var(--yellow)" d="M0,338 C180,275 420,228 700,203 L700,222 C420,242 180,287 0,345 Z"/>
      <path fill="var(--red)" d="M330,243 C480,214 600,198 700,176 L700,192 C600,210 480,228 330,243 Z"/>
    </svg>

    <div class="brand">
      <span class="brand-dot"></span>
      <span class="brand-name">Bright Lane Haulage</span>
    </div>

    <address class="contact">
      <div class="contact-phone">1800 BL Haul</div>
      <div class="contact-address">4/7 Ashgrove Court, VIC 3521</div>
      <div class="contact-email">move@BrightLaneHaulage.com.au</div>
    </address>
  </section>
</main>
</body>
</html>
```